A world class design for a " Discount services provider"
Brightfold Savings Network International
A world class design for a " Discount services provider" - Financial Services
Creative Brief
Simple
Kemi ARUBA
Managing Partner
Suite 204, 306 & 118, Corlenne Plaza, Opp. Former Harbour Works Bureau, Tesvara Crescent , Zone 8, Ilumo Abuja - FCT
infokemiaruba@brightfoldmail.example
www.brightfoldsavingsnet.example
The back of the business card should carry my detailed imformation, while the front should carry only the company's designed logo and colour.
Tavolin Tavolin
Dear Designers, Thank you for the wonderful work you have submitted so far. Looking forward to see more beautiful and creative designs though. Great minds!
Dear Designers, Please remember that I also need the following Stationary designs in addtion to the business card design. 1. Letterhead (A4 Size 210mm x 297mm) 2. Envelope (C4 Size 229mmx324mm) 3. Email Signature

```html
<!DOCTYPE html>
<html lang="en">
<head>
<meta charset="utf-8">
<title>Brightfold Savings Network International – Business Card</title>
<link rel="stylesheet" href="https://fonts.googleapis.com/css2?family=PT+Sans:wght@400;700&display=swap">
<style>
  :root {
    --bg: #e9eaec;
    --card: #ffffff;
    --navy: #1f3f7a;
    --blue: #2a5bbf;
    --blue-light: #5b8be0;
    --ink: #222222;
    --black: #0c0c0c;
    --shadow: rgba(0, 0, 0, 0.25);
  }
  * { margin: 0; padding: 0; box-sizing: border-box; }
  html, body { width: 1200px; height: 902px; overflow: hidden; }
  body {
    background: var(--bg);
    font-family: "PT Sans", Arial, sans-serif;
    position: relative;
  }
  .card {
    position: absolute;
    width: 600px;
    height: 345px;
    background: var(--card);
    border-radius: 10px;
    box-shadow: 0 10px 30px var(--shadow);
    overflow: hidden;
  }
  .card--front { left: 90px; top: 60px; }
  .card--back { left: 510px; top: 497px; }

  .brand {
    display: flex;
    align-items: center;
    gap: 10px;
    color: var(--navy);
  }
  .brand__dot {
    flex: none;
    width: 34px;
    height: 34px;
    border-radius: 50%;
    background: var(--navy);
  }
  .brand__name {
    font-weight: 700;
    text-transform: uppercase;
    line-height: 1.15;
    letter-spacing: 0.02em;
  }

  .card--front .brand {
    position: absolute;
    left: 50%;
    top: 125px;
    transform: translateX(-50%);
    width: 330px;
  }
  .card--front .brand__name { font-size: 17px; }
  .front__web {
    position: absolute;
    left: 0; right: 0;
    top: 215px;
    text-align: center;
    font-size: 16px;
    color: var(--ink);
    letter-spacing: 0.03em;
  }

  .card--back .brand {
    position: absolute;
    left: 40px;
    top: 95px;
    width: 250px;
  }
  .card--back .brand__name { font-size: 14px; }
  .holder {
    position: absolute;
    right: 34px;
    top: 32px;
    text-align: right;
  }
  .holder__name { font-size: 21px; color: var(--navy); font-weight: 700; }
  .holder__title { font-size: 14px; color: var(--ink); margin-top: 2px; }

  .contact {
    position: absolute;
    right: 34px;
    top: 192px;
    list-style: none;
    text-align: right;
    font-size: 15px;
    color: var(--ink);
  }
  .contact li { display: flex; justify-content: flex-end; align-items: center; gap: 7px; line-height: 21px; }
  .contact svg { width: 11px; height: 11px; fill: var(--navy); }

  .swoosh { position: absolute; left: 0; bottom: 0; width: 600px; height: 120px; }
</style>
</head>
<body>

<section class="card card--front" aria-label="Business card front">
  <div class="brand">
    <span class="brand__dot"></span>
    <span class="brand__name">Brightfold Savings Network International</span>
  </div>
  <p class="front__web">www.yoursitename.example</p>
</section>

<section class="card card--back" aria-label="Business card back">
  <div class="brand">
    <span class="brand__dot"></span>
    <span class="brand__name">Brightfold Savings Network International</span>
  </div>

  <div class="holder">
    <p class="holder__name">Dario Fenwick</p>
    <p class="holder__title">Managing Director</p>
  </div>

  <ul class="contact">
    <li>123 456 7890
      <svg viewBox="0 0 24 24" aria-hidden="true"><path d="M6.6 10.8a15.1 15.1 0 0 0 6.6 6.6l2.2-2.2a1 1 0 0 1 1-.25 11.4 11.4 0 0 0 3.6.57 1 1 0 0 1 1 1V20a1 1 0 0 1-1 1A17 17 0 0 1 3 4a1 1 0 0 1 1-1h3.5a1 1 0 0 1 1 1c0 1.25.2 2.45.57 3.6a1 1 0 0 1-.25 1z"/></svg>
    </li>
    <li>123 456 7890
      <svg viewBox="0 0 24 24" aria-hidden="true"><path d="M6 2h10v6H6zM3 9h18v9h-3v4H6v-4H3zm5 7v4h8v-4z"/></svg>
    </li>
    <li>yourname@mailbox.example
      <svg viewBox="0 0 24 24" aria-hidden="true"><path d="M2 5h20v14H2zm2 2v.5l8 5 8-5V7z"/></svg>
    </li>
  </ul>

  <svg class="swoosh" viewBox="0 0 600 120" preserveAspectRatio="none" aria-hidden="true">
    <defs>
      <linearGradient id="blueBand" x1="0" y1="0" x2="1" y2="0">
        <stop offset="0" stop-color="var(--blue-light)"/>
        <stop offset="1" stop-color="var(--blue)"/>
      </linearGradient>
    </defs>
    <path d="M0 40 C120 20 260 40 360 120 L0 120 Z" fill="var(--black)"/>
    <path d="M0 62 C130 45 250 70 330 120 L0 120 Z" fill="url(#blueBand)"/>
    <path d="M0 100 C200 100 400 110 600 100 L600 120 L0 120 Z" fill="var(--black)"/>
  </svg>
</section>

</body>
</html>
```